Marlow Estates Business Card and Email Signature Design

I am a Homevant and need a business card design with my head shot picture and logo and contact information that can be prepared to be used on my email signature as well. I would like my head shot image background to match the background of the business card. So in other words the background of my head shot should be transparent. I would like the Homevant Logo on there and also PRX and Fair Dwelling Logo. My email address is: ted@marlowestates.example, Phone Number is: 555-014-7391, website: www.marlowestates.example Address: 48207 Quillfern Court Ashvale, NT 40917
I also need just the head shot photo with white background in a JPEG file as well so I can upload that picture to my Jobtrellis and Nestavo profiles.

```html
<!DOCTYPE html>
<html lang="en">
<head>
<meta charset="utf-8">
<title>Marlow Estates Business Card</title>
<link rel="stylesheet" href="https://fonts.googleapis.com/css2?family=Open+Sans:wght@400;600;700&display=swap">
<style>
  :root {
    --blue: #14628f;
    --blue-deep: #0b3c5f;
    --blue-tab: #1f6e9b;
    --stripe: #4a4c50;
    --ink: #3a3b3e;
    --paper: #ffffff;
    --paper-shade: #eceef0;
    --backdrop: #e8e5e0;
  }
  * { box-sizing: border-box; margin: 0; padding: 0; }
  html, body { width: 771px; height: 1200px; overflow: hidden; }
  body {
    background: var(--backdrop);
    font-family: "Open Sans", Arial, sans-serif;
    position: relative;
  }
  .card {
    position: absolute;
    top: 320px;
    width: 330px;
    height: 560px;
    border-radius: 18px;
    overflow: hidden;
    background: linear-gradient(180deg, var(--paper) 0%, var(--paper-shade) 100%);
    box-shadow: 0 6px 18px rgba(0,0,0,0.18);
  }
  .card--front { left: 40px; }
  .card--back { left: 401px; }

  /* Front */
  .headshot {
    position: absolute; left: 35px; top: 70px; width: 260px; height: 330px;
    border-radius: 120px 120px 0 0;
    background: linear-gradient(180deg, #d6c2b4 0%, #b9a294 35%, #6d7f95 60%, #2c3c52 100%);
  }
  .front-band {
    position: absolute; left: 0; right: 0; bottom: 0; height: 270px;
    background: linear-gradient(180deg, rgba(20,98,143,0) 0%, var(--blue) 45%, var(--blue-deep) 100%);
  }
  .front-logo {
    position: absolute; top: 26px; right: 22px;
    display: flex; align-items: center; gap: 6px;
    color: var(--blue); font-weight: 700; font-size: 12px;
  }
  .logo-dot { width: 26px; height: 26px; border-radius: 50%; background: var(--blue); flex: none; }
  .front-name {
    position: absolute; left: 30px; bottom: 70px;
    color: #fff; font-size: 36px; font-weight: 400; line-height: 1;
  }
  .front-title {
    position: absolute; left: 58px; bottom: 40px;
    color: #fff; font-size: 20px;
  }

  /* Back */
  .back-stripe {
    position: absolute; top: 0; bottom: 0; left: 50px; width: 30px;
    background: var(--stripe);
  }
  .back-logo {
    position: absolute; top: 34px; right: 20px; text-align: right;
  }
  .back-logo .brand {
    display: flex; align-items: center; justify-content: flex-end; gap: 6px;
    color: var(--blue); font-weight: 700; font-size: 18px; text-transform: uppercase;
  }
  .back-logo .tagline {
    font-size: 8px; letter-spacing: 1.5px; color: var(--ink); font-weight: 600; margin-top: 2px;
  }
  .back-name {
    position: absolute; left: 98px; top: 100px;
    font-size: 24px; font-weight: 600; color: var(--ink);
  }
  .back-title {
    position: absolute; left: 98px; top: 132px;
    font-size: 14px; color: var(--blue);
  }
  .contacts { position: absolute; left: 36px; top: 180px; right: 12px; list-style: none; }
  .contact { display: flex; align-items: flex-start; gap: 18px; height: 66px; }
  .contact-tab {
    flex: none; width: 58px; height: 40px; background: var(--blue-tab);
    display: flex; align-items: center; justify-content: center;
    box-shadow: 0 2px 4px rgba(0,0,0,0.25);
  }
  .contact-tab svg { width: 20px; height: 20px; }
  .icon-fill { fill: #fff; }
  .icon-line { fill: none; stroke: #fff; stroke-width: 1.8; }
  .contact-text { font-size: 13px; color: var(--ink); padding-top: 10px; line-height: 1.3; white-space: nowrap; }
  .contact-text::after {
    content: ""; display: block; width: 100px; height: 2px; background: var(--blue); margin-top: 8px;
  }
  .badges {
    position: absolute; right: 22px; bottom: 24px; display: flex; gap: 8px; align-items: center;
  }
  .badge { width: 26px; height: 26px; border: 2px solid var(--ink); border-radius: 3px; }
  .badge--wide { width: 40px; }
</style>
</head>
<body>
  <section class="card card--front">
    <div class="headshot" role="img" aria-label="Agent headshot on transparent background"></div>
    <div class="front-band"></div>
    <div class="front-logo"><span class="logo-dot"></span>Marlow Estates</div>
    <p class="front-name">Your Name</p>
    <p class="front-title">Job Title</p>
  </section>

  <section class="card card--back">
    <div class="back-stripe"></div>
    <div class="back-logo">
      <div class="brand"><span class="logo-dot"></span>Marlow Estates</div>
      <div class="tagline">REAL ESTATE SERVICES</div>
    </div>
    <p class="back-name">Your Name</p>
    <p class="back-title">Job title</p>
    <ul class="contacts">
      <li class="contact">
        <span class="contact-tab"><svg viewBox="0 0 24 24"><path class="icon-fill" d="M6.6 10.8a15 15 0 0 0 6.6 6.6l2.2-2.2a1 1 0 0 1 1-.25 11.4 11.4 0 0 0 3.6.57 1 1 0 0 1 1 1V20a1 1 0 0 1-1 1A17 17 0 0 1 3 4a1 1 0 0 1 1-1h3.5a1 1 0 0 1 1 1 11.4 11.4 0 0 0 .57 3.6 1 1 0 0 1-.25 1z"/></svg></span>
        <span class="contact-text">555-014-7391</span>
      </li>
      <li class="contact">
        <span class="contact-tab"><svg viewBox="0 0 24 24"><rect class="icon-line" x="3" y="5.5" width="18" height="13" rx="1"/><path class="icon-line" d="M3.5 6.5 12 13l8.5-6.5"/></svg></span>
        <span class="contact-text">ted@marlowestates.example</span>
      </li>
      <li class="contact">
        <span class="contact-tab"><svg viewBox="0 0 24 24"><circle class="icon-line" cx="12" cy="12" r="9"/><ellipse class="icon-line" cx="12" cy="12" rx="4" ry="9"/><path class="icon-line" d="M3 12h18M5 7.5h14M5 16.5h14"/></svg></span>
        <span class="contact-text">www.marlowestates.example</span>
      </li>
      <li class="contact">
        <span class="contact-tab"><svg viewBox="0 0 24 24"><path class="icon-fill" d="M12 2a7 7 0 0 0-7 7c0 5 7 13 7 13s7-8 7-13a7 7 0 0 0-7-7zm0 9.5A2.5 2.5 0 1 1 12 6.5a2.5 2.5 0 0 1 0 5z"/></svg></span>
        <span class="contact-text">48207 Quillfern Court Ashvale<br>NT 40917</span>
      </li>
    </ul>
    <div class="badges">
      <span class="badge"></span>
      <span class="badge badge--wide"></span>
      <span class="badge"></span>
    </div>
  </section>
</body>
</html>
```